VORELL'S BRAND-PACKAGING DESIGN FOR A CHAMOY PICKLE IN A POUCH

This is a project for Corinne Vorell from Flickpop. WE ARE CREATING A PACKAGING DESIGN FOR A PICKLE IN A POUCH. OUR FIRST RELEASE WILL BE FOR A CHAMOY FLAVORED-RED PICKLE IN A POUCH. THIS IS FOR CRAZY PICKLE FLAVORS (MAINLY CHAMOY PICKLE); WE WANT THE DESIGN TO HAVE FUN AND PLAYFUL VIBE. WE WANT IT TO POP. WE LIKE VIBRANT COLORS THESE TYPES OF PICKLES ARE NORMALLY EATEN WITH CANDY (MOSTLY MEXICAN CANDY) IN THEM, WHICH IS WHAT MAKES THEM SO POPULAR AND UNIQUE.

WE WILL NEED A FRONT DESIGN AND A BACK DESIGN OF THE PICKLE POUCH.

IMAGE MEASUREMENTS ARE: 4.5 INCHES x 9 INCHES

THE ACTUAL LOOK AND SHAPE OF THE POUCH IS IN THE PHOTOS WITH THE TAPE MEASURE IN THEM.

FRONT OF PACKAGE DESIGN:
TEAR LINE ONE INCH FROM TOP: PLEASE SEE PHOTOS

BACK OF PACKAGE DESIGN:
LEAVE EXTRA ROOM ON THE BACK DESIGN. IT WILL HAVE A BARCODE ON IT AS WELL AS A QR CODE, NUTRITION LABEL ,INGREDIENTS AND COMPANY INFO WHICH WE WILL ADD LATER.

Font styles to use
Other font styles liked:
• bubble letters, something fun

Colors
FFF300
FFF600
FEFA6F
FFFEC7
FFFEE8
EB3D1F
EC4F4E
F09395
F8D3D4
FCEDEE
E54698
E96AAD
F1A4CE
F9D9EA
FCEFF6

Requirements
Must have
• bright colors, not pastle colors. we want the same vibe as the ay rulo chamoy candy (photos attached)
Nice to have
• Can you include some designs with a cartoon character of Corinne Vorell's face (photos attached) on the packaging? Maybe of her holding a red pickle with pickle juice dripping from it; you can look at her flick pop as well: @c_vorell

```html
<!DOCTYPE html>
<html lang="en">
<head>
<meta charset="utf-8">
<title>Vorell's Chamoy Dill Pickle Pouch – Front</title>
<link href="https://fonts.googleapis.com/css2?family=Fredoka:wght@700&family=Roboto+Condensed:wght@500&family=Open+Sans:wght@400&display=swap" rel="stylesheet">
<style>
  :root {
    --stage: #2b2b29;
    --pouch-black: #1c1c1c;
    --chamoy-red: #d8262e;
    --chamoy-deep: #8e1a1f;
    --pickle-red: #a5232a;
    --sun-yellow: #fff300;
    --soft-yellow: #fefa6f;
    --window-white: #f4f4f2;
    --dill-green: #3f9a3c;
    --ink-white: #ffffff;
  }
  html, body {
    margin: 0;
    padding: 0;
    width: 1050px;
    height: 1200px;
    overflow: hidden;
    background: var(--stage);
  }
  .canvas {
    position: relative;
    width: 1050px;
    height: 1200px;
  }
  .pouch {
    position: absolute;
    left: 255px;
    top: 60px;
    width: 540px;
    height: 1080px;
  }
  .tear-note {
    font-family: "Open Sans", sans-serif;
    font-size: 13px;
    fill: var(--ink-white);
  }
  .brand-name {
    font-family: "Fredoka", sans-serif;
    font-weight: 700;
    font-size: 78px;
    fill: var(--chamoy-red);
  }
  .product-title {
    font-family: "Fredoka", sans-serif;
    font-weight: 700;
    fill: var(--ink-white);
    stroke: var(--dill-green);
    stroke-width: 4px;
    paint-order: stroke;
  }
  .product-note {
    font-family: "Roboto Condensed", sans-serif;
    font-weight: 500;
    font-size: 17px;
    fill: var(--ink-white);
    letter-spacing: 0.5px;
  }
</style>
</head>
<body>
<main class="canvas">
  <svg class="pouch" viewBox="0 0 540 1080" xmlns="http://www.w3.org/2000/svg">
    <defs>
      <clipPath id="pouch-shape">
        <path d="M20 0 H520 Q540 0 540 20 V1080 H0 V20 Q0 0 20 0 Z"/>
      </clipPath>
      <radialGradient id="pickle-tone" cx="50%" cy="50%" r="60%">
        <stop offset="0%" stop-color="#b7262c" stop-opacity="0.95"/>
        <stop offset="100%" stop-color="#7f161b" stop-opacity="0.9"/>
      </radialGradient>
    </defs>

    <g clip-path="url(#pouch-shape)">
      <!-- upper black field -->
      <rect class="field-black" x="0" y="0" width="540" height="1080" fill="var(--pouch-black)"/>

      <!-- red middle band with soft curve -->
      <path class="field-red" d="M0 470 Q90 380 180 440 Q270 500 360 430 Q450 370 540 450 V760 H0 Z" fill="var(--chamoy-red)"/>

      <!-- bottom yellow field -->
      <path class="field-yellow" d="M0 740 Q270 640 540 740 V1080 H0 Z" fill="var(--sun-yellow)"/>

      <!-- clear window -->
      <path class="window" d="M30 780 Q270 690 510 780 V930 Q270 1010 30 930 Z" fill="var(--window-white)"/>

      <!-- top corner accents -->
      <circle cx="505" cy="5" r="38" fill="var(--sun-yellow)"/>
      <ellipse cx="110" cy="-4" rx="60" ry="18" fill="var(--sun-yellow)"/>
    </g>

    <!-- pickle photo area -->
    <ellipse class="pickle-photo" role="img" aria-label="Photo of a red chamoy-coated dill pickle"
             cx="270" cy="600" rx="210" ry="470" fill="url(#pickle-tone)" opacity="0.9"/>

    <!-- hang hole -->
    <rect x="218" y="30" width="104" height="26" rx="13" fill="#111"/>

    <!-- zipper / tear lines -->
    <line x1="0" y1="82" x2="540" y2="82" stroke="#3a3a3a" stroke-width="2"/>
    <line x1="0" y1="132" x2="540" y2="132" stroke="#3a3a3a" stroke-width="3"/>
    <line x1="0" y1="140" x2="540" y2="140" stroke="#3a3a3a" stroke-width="2"/>

    <text class="tear-note" x="270" y="115" text-anchor="middle">tear here to discover our delicious natural mainly chamoy pickle</text>

    <!-- brand name -->
    <text class="brand-name" x="270" y="275" text-anchor="middle">Vorell's</text>

    <!-- product title -->
    <text class="product-title" x="270" y="455" text-anchor="middle" font-size="70" transform="rotate(-3 270 455)">Chamoy Dill</text>
    <rect class="pickle-icon" role="img" aria-label="Small green pickle illustration" x="245" y="478" width="52" height="22" rx="11" fill="var(--dill-green)" transform="rotate(-20 271 489)"/>
    <text class="product-title" x="270" y="585" text-anchor="middle" font-size="84">Pickle</text>

    <text class="product-note" x="270" y="650" text-anchor="middle" transform="rotate(2 270 650)">Contents: 1 Pickle&#160;&#160;I&#160;&#160;Made with Real Dill!</text>

    <line x1="240" y1="935" x2="300" y2="935" stroke="var(--ink-white)" stroke-width="3"/>

    <text class="product-note" x="270" y="1045" text-anchor="middle" transform="rotate(-4 270 1045)">No Refrigeration Needed</text>
  </svg>
</main>
</body>
</html>
```